Conservative, Modern and Sharp Builder Business card

Hi there,
We would like to update our existing business card.
I have attached photos of existing business card, logo and van sign.

I would like the business card to also list what we do :
Renovation • New Build • Alteration
Extension • Bathroom • Maintenance.(Seperated by dots)

Contact number : 021 0483 0752
(With that exact spacing)

Ideally when people looking from about 2-3 metres, they know that it is a builder’s business card

Open to suggestions on fonts, layout, style of business card

PLEASE ONLY SUBMIT YOUR BEST OR MAX 3 DESIGNS FOR EACH DESIGNER

Thanks

Industry/Entity Type

Construction. Renovation

Contact Information for Business Card

Details should be the same as the existing card. And addition of what we do.

Requirements
Should not have
• The new business card must not have the same layout as our existing one. Thanks

```html
<!DOCTYPE html>
<html lang="en">
<head>
<meta charset="utf-8">
<title>FlintBuild Business Card</title>
<link href="https://fonts.googleapis.com/css2?family=Open+Sans:wght@400;600;800&family=Crimson+Text:ital,wght@1,400;1,600&display=swap" rel="stylesheet">
<style>
  :root {
    --backdrop: #e4e4e6;
    --card: #ffffff;
    --ink: #111111;
    --muted: #6a6a6a;
    --rule: #555555;
  }
  * { box-sizing: border-box; margin: 0; padding: 0; }
  html, body {
    width: 1200px; height: 800px; overflow: hidden;
    background: var(--backdrop);
    font-family: "Open Sans", Arial, sans-serif;
    color: var(--ink);
  }
  .sheet {
    width: 1200px; height: 800px;
    display: flex; align-items: center; justify-content: center; gap: 50px;
  }
  .card {
    position: relative;
    width: 540px; height: 310px;
    background: var(--card);
    box-shadow: 0 6px 18px rgba(0,0,0,0.12);
    overflow: hidden;
  }
  .wordmark {
    position: absolute;
    display: flex; align-items: center; gap: 8px;
    font-family: "Open Sans", Arial, sans-serif;
    font-weight: 800; font-size: 34px; letter-spacing: -0.5px;
    color: var(--ink);
  }
  .wordmark-square { width: 14px; height: 14px; background: var(--ink); }

  /* Front: services */
  .card-front .wordmark { right: 38px; top: 120px; }
  .card-front .divider {
    position: absolute; left: 90px; right: 30px; top: 182px;
    height: 1px; background: var(--rule);
  }
  .services {
    position: absolute; left: 90px; top: 192px;
    font-family: "Crimson Text", Georgia, serif; font-style: italic;
    font-size: 21px; line-height: 1.25; color: #333;
  }
  .services li { list-style: none; display: flex; align-items: center; gap: 7px; }
  .sep { width: 9px; height: 9px; fill: var(--ink); }

  /* Back: contact */
  .card-back .person { position: absolute; left: 34px; top: 40px; }
  .person-name { font-weight: 600; font-size: 15px; letter-spacing: 1px; text-transform: uppercase; }
  .person-role { font-size: 13px; color: var(--muted); margin-top: 2px; }
  .card-back .divider {
    position: absolute; left: 170px; right: 26px; top: 86px;
    height: 1px; background: var(--rule);
  }
  .contacts { position: absolute; left: 34px; top: 100px; list-style: none; }
  .contacts li {
    display: flex; align-items: center; gap: 8px;
    font-size: 13px; color: var(--muted); line-height: 22px;
  }
  .contacts li.phone { font-family: "Crimson Text", Georgia, serif; font-weight: 600; font-style: normal; font-size: 19px; color: var(--ink); }
  .icon { width: 13px; height: 13px; fill: none; stroke: var(--ink); stroke-width: 1.6; }
  .card-back .wordmark { right: 40px; top: 150px; }
  .card-back .rule-bottom {
    position: absolute; left: 250px; right: 26px; top: 236px;
    height: 1px; background: var(--rule);
  }
</style>
</head>
<body>
<main class="sheet">
  <section class="card card-front" aria-label="Business card front">
    <div class="wordmark"><span class="wordmark-square"></span>FlintBuild</div>
    <div class="divider"></div>
    <ul class="services">
      <li>Renovation <svg class="sep" viewBox="0 0 10 10"><polygon points="5,0 10,10 0,10"/></svg> New Build <svg class="sep" viewBox="0 0 10 10"><polygon points="5,0 10,10 0,10"/></svg> Alteration</li>
      <li>Extension <svg class="sep" viewBox="0 0 10 10"><polygon points="5,0 10,10 0,10"/></svg> Bathroom <svg class="sep" viewBox="0 0 10 10"><polygon points="5,0 10,10 0,10"/></svg> Maintenance</li>
    </ul>
  </section>

  <section class="card card-back" aria-label="Business card back">
    <div class="person">
      <p class="person-name">Daniel Hartono</p>
      <p class="person-role">Residential Builder</p>
    </div>
    <div class="divider"></div>
    <ul class="contacts">
      <li class="phone"><svg class="icon" viewBox="0 0 14 14"><path d="M3 1.5 L5.5 1.5 L6.5 4.5 L5 5.5 Q6 8.5 8.5 9 L9.5 7.5 L12.5 8.5 L12.5 11 Q7 12.5 3.5 8 Q1.5 5 3 1.5 Z"/></svg>021 0483 0752</li>
      <li><svg class="icon" viewBox="0 0 14 14"><rect x="1.5" y="3" width="11" height="8"/><path d="M1.5 3 L7 7.5 L12.5 3"/></svg>FlintBuild@mailbox.nz</li>
      <li><svg class="icon" viewBox="0 0 14 14"><circle cx="7" cy="7" r="5.5"/><path d="M1.5 7 H12.5 M7 1.5 Q4 7 7 12.5 Q10 7 7 1.5"/></svg>www.FlintBuild.nz</li>
      <li><svg class="icon" viewBox="0 0 14 14"><circle cx="7" cy="7" r="5.5"/></svg>FlintBuild.nz</li>
    </ul>
    <div class="wordmark"><span class="wordmark-square"></span>FlintBuild</div>
    <div class="rule-bottom"></div>
  </section>
</main>
</body>
</html>
```